Purchase Protection Subscription Program needs a refreshed website

We are refreshing an existing website www.carevaultplus.example. This is a purchase protection product which allows its members to receive extended warranty on the items they buy, receive a rebate of 50% on a repair of an item, a personal shopping concierge, etc. We are looking for a fresh, clean approach - with mass appeal to both men and woman. The site should convey trust, and ease of use.

Thanks to everyone who posted designs. Amazing work! It was a very difficult decision!

```html
<!DOCTYPE html>
<html lang="en">
<head>
<meta charset="utf-8">
<title>CareVault Plus — Shop with confidence</title>
<link href="https://fonts.googleapis.com/css2?family=Oswald:wght@500;600&family=Roboto+Condensed:wght@400;700&family=Lato:wght@400;700&display=swap" rel="stylesheet">
<style>
:root{
  --red:#d7171f;
  --red-dark:#a80f15;
  --ink:#222;
  --text:#444;
  --muted:#666;
  --light:#f1f1f1;
  --line:#dcdcdc;
  --footer:#3a3a3a;
  --footer-bottom:#2b2b2b;
  --footer-text:#e6e6e6;
  --green:#3fa63f;
}
*{box-sizing:border-box;margin:0;padding:0}
html,body{width:806px;height:1200px;overflow:hidden;background:#fff}
body{position:relative;font-family:"Lato",sans-serif;color:var(--text)}
.abs{position:absolute}
.cond{font-family:"Roboto Condensed",sans-serif}

/* header */
.header{left:0;top:0;width:806px;height:62px;background:linear-gradient(#fff,#f4f4f4);border-bottom:1px solid #ddd}
.brand{left:95px;top:20px;font-family:"Lato",sans-serif;font-size:21px;color:#222;display:flex;align-items:center;gap:7px}
.brand-dot{width:12px;height:12px;background:var(--red);display:inline-block}
.topbar{right:95px;top:7px;display:flex;align-items:center;gap:6px}
.phone{color:var(--red);font-size:12px;font-family:"Roboto Condensed",sans-serif;display:flex;align-items:center;gap:4px;margin-right:6px}
.topbtn{background:#666;color:#fff;font-size:9px;padding:3px 6px;font-weight:700}
.nav{right:95px;top:38px;display:flex;align-items:center;font-family:"Roboto Condensed",sans-serif;font-size:9.5px;font-weight:700;color:#333}
.nav a{color:#333;text-decoration:none;padding:3px 13px;border-left:1px solid #ddd}
.nav a:first-child{border:0}
.nav a.active{background:var(--red);color:#fff;border-radius:2px;padding:3px 9px;margin-right:9px}

/* hero */
.hero{left:0;top:62px;width:806px;height:290px}
.hero-copy{left:433px;top:112px;width:280px}
.rule{border-top:1px dotted #888;width:275px}
.kicker{font-family:"Lato",sans-serif;font-weight:700;font-size:16px;color:#222;margin-top:11px}
.headline{font-family:"Oswald",sans-serif;font-weight:600;font-size:35px;color:var(--red);line-height:1.05;margin-top:1px;letter-spacing:-.3px}
.sub{font-family:"Lato",sans-serif;font-weight:700;font-size:18px;color:#222;margin:6px 0 9px 3px}
.checks{list-style:none;margin-top:11px;font-family:"Roboto Condensed",sans-serif;font-size:11px;color:#333}
.checks li{display:flex;align-items:center;gap:6px;margin-bottom:10px}
.btn-dark{display:inline-block;background:linear-gradient(#333,#111);color:#fff;font-family:"Lato",sans-serif;font-weight:700;font-size:12px;padding:8px 20px;margin-top:16px}

/* feature cards */
.card{top:383px;width:195px;height:112px;background:linear-gradient(#fff,#ececec);border:1px solid #ddd;box-shadow:0 4px 4px -2px rgba(0,0,0,.25)}
.card .icon{left:8px;top:24px;width:50px;height:50px;border-radius:50%;background:var(--red);border:3px solid #eee;box-shadow:0 0 0 1px #ccc}
.card h3{left:67px;top:5px;width:125px;font-family:"Roboto Condensed",sans-serif;font-size:14px;color:var(--red);line-height:1.1;font-weight:400}
.card p{left:67px;top:40px;width:125px;font-size:7.8px;line-height:1.5;color:#555}
.card .more{left:67px;top:87px;background:#222;color:#fff;font-size:8px;padding:3px 8px;font-family:"Lato",sans-serif}

/* welcome */
.welcome{left:0;top:527px;width:806px;height:198px;background:var(--light)}
.welcome h2{left:95px;top:16px;font-family:"Roboto Condensed",sans-serif;font-size:19px;color:#222;font-weight:400}
.welcome h2 span{color:var(--red)}
.video{left:95px;top:55px;width:190px;height:117px;border:2px solid #333;background:linear-gradient(135deg,#8c8a73,#c9b99a 50%,#6d7b6c)}
.video-bar{left:0;bottom:0;width:100%;height:13px;background:#222}
.welcome p.body{left:299px;top:53px;width:199px;font-size:8.3px;line-height:1.72;color:#555}
.read-more{left:448px;top:168px;font-size:8px;font-weight:700;text-decoration:underline;color:#333}
.pf{left:525px;top:20px;width:188px}
.pf-head{height:29px;width:188px;background:var(--red);color:#fff;font-family:"Roboto Condensed",sans-serif;font-size:15px;padding:5px 0 0 8px;clip-path:polygon(0 0,93% 0,100% 50%,93% 100%,0 100%)}
.pf ul{list-style:none;background:#fff;width:174px;border:1px solid var(--line)}
.pf li{height:26.5px;border-bottom:1px solid var(--line);display:flex;align-items:center;gap:6px;padding-left:11px;font-size:9.6px;color:#333}
.pf li:last-child{border:0}

/* how it works */
.how-line{left:95px;top:770px;width:617px;border-top:1px solid #ddd}
.how-title{left:326px;top:757px;width:154px;height:27px;background:var(--red);color:#fff;font-family:"Roboto Condensed",sans-serif;font-size:15.5px;text-align:center;line-height:27px;clip-path:polygon(0 0,100% 0,96% 50%,100% 100%,0 100%,4% 50%)}
.step{top:809px;width:104px;height:104px;border-radius:50%;background:radial-gradient(circle at 50% 40%,#8a8a8a,#5f5f5f);border:3px solid #ddd;box-shadow:0 8px 8px -6px rgba(0,0,0,.35)}
.step-label{top:930px;width:160px;text-align:center;font-family:"Roboto Condensed",sans-serif;font-size:15.5px;line-height:1.25;color:#333}
.step-label span{color:var(--red)}

/* footer */
.footer{left:0;top:1003px;width:806px;height:169px;background:var(--footer);border-top:2px solid var(--red)}
.fcol{top:1024px}
.fcol h4{font-family:"Roboto Condensed",sans-serif;font-size:11px;color:#fff;font-weight:700;padding-bottom:7px;border-bottom:1px solid #555;margin-bottom:9px}
.links{list-style:none;font-size:8.5px;color:var(--footer-text)}
.links li{margin-bottom:9.5px}
.links li::before{content:"›";margin-right:5px;color:#aaa}
.field{width:148px;height:18px;background:#fff;margin-bottom:5px;font-size:8.5px;color:#444;display:flex;align-items:center;gap:8px;padding-left:7px}
.field.tall{height:38px;align-items:flex-start;padding-top:5px}
.subscribe{display:inline-block;background:var(--red);color:#fff;font-size:7.5px;font-weight:700;padding:3px 7px;margin-top:2px}
.map{width:155px;height:104px;border:3px solid #fff;background:linear-gradient(140deg,#dfe6c9,#b8d3e6 45%,#e8e4d6 70%,#a8c7e0)}
.info{font-size:8.5px;color:var(--footer-text);line-height:1.45}
.info .row{display:flex;gap:10px;margin-bottom:7px}
.info svg{flex:none}
.bottombar{left:0;top:1172px;width:806px;height:28px;background:var(--footer-bottom);font-size:8.5px;color:#ddd}
.copy{left:98px;top:9px}
.follow{right:118px;top:9px;display:flex;gap:8px;align-items:center}
</style>
</head>
<body>

<header class="abs header">
  <div class="abs brand"><span class="brand-dot"></span>CareVault Plus</div>
  <div class="abs topbar">
    <span class="phone">
      <svg width="11" height="11" viewBox="0 0 24 24"><path fill="#3fa63f" d="M6.6 10.8a15 15 0 0 0 6.6 6.6l2.2-2.2c.3-.3.7-.4 1-.2 1.1.4 2.3.6 3.6.6.6 0 1 .4 1 1V20c0 .6-.4 1-1 1A17 17 0 0 1 3 4c0-.6.4-1 1-1h3.5c.6 0 1 .4 1 1 0 1.3.2 2.5.6 3.6.1.3 0 .7-.2 1z"/></svg>
      (888) 555-0142</span>
    <span class="topbtn">Register</span>
    <span class="topbtn">Log in</span>
  </div>
  <nav class="abs nav">
    <a class="active">HOME</a><a>ABOUT US</a><a>PRODUCT FEATURES</a><a>HOW IT WORKS</a><a>CONTACT</a>
  </nav>
</header>

<section class="abs hero">
  <svg width="806" height="290" viewBox="0 0 806 290">
    <defs>
      <linearGradient id="heroBg" x1="0" x2="1"><stop offset="0" stop-color="#f1f1f1"/><stop offset="1" stop-color="#e4e4e4"/></linearGradient>
      <linearGradient id="shoppers" x1="0" y1="0" x2="1" y2="1"><stop offset="0" stop-color="#b59a78"/><stop offset=".5" stop-color="#8f9aa3"/><stop offset="1" stop-color="#c7c0b3"/></linearGradient>
    </defs>
    <rect width="806" height="290" fill="url(#heroBg)"/>
    <path d="M0 0H478C420 40 378 150 364 290H0Z" fill="#c71119"/>
    <path role="img" aria-label="Photo: group of friends walking with colourful shopping bags" d="M0 0H466C410 45 368 150 354 290H0Z" fill="url(#shoppers)"/>
  </svg>
</section>

<div class="abs hero-copy">
  <div class="rule"></div>
  <div class="kicker">SHOP WITH CONFIDENCE KNOWING</div>
  <div class="headline">CAREVAULT PLUS</div>
  <div class="sub">IS THERE</div>
  <div class="rule"></div>
  <ul class="checks">
    <li><svg width="9" height="9" viewBox="0 0 10 10"><path d="M1 5l3 3 5-7" stroke="#3fa63f" stroke-width="2" fill="none"/></svg>Semper eu enim quis lobortis mollis ipum</li>
    <li><svg width="9" height="9" viewBox="0 0 10 10"><path d="M1 5l3 3 5-7" stroke="#3fa63f" stroke-width="2" fill="none"/></svg>Tation ullorper suscipit lobortis nislalquip</li>
  </ul>
  <span class="btn-dark">LEARN MORE</span>
</div>

<!-- feature cards -->
<div class="abs card" style="left:95px">
  <svg class="abs icon" viewBox="0 0 50 50"><path d="M25 11l11 4v8c0 8-5 13-11 16-6-3-11-8-11-16v-8z" fill="none" stroke="#fff" stroke-width="2.5"/><path d="M19 25l4 4 8-9" stroke="#fff" stroke-width="2.5" fill="none"/></svg>
  <h3 class="abs">VALUABLE PURCHASE PROTECTION</h3>
  <p class="abs">Get 5 unique ways to get more out of the things you buy:*<br><b style="font-size:10px;color:#333;line-height:2">☑ Warranty extension</b></p>
  <span class="abs more">READ MORE</span>
</div>
<div class="abs card" style="left:306px">
  <svg class="abs icon" viewBox="0 0 50 50"><rect x="17" y="12" width="16" height="24" rx="2" fill="none" stroke="#fff" stroke-width="2.2"/><path d="M20 19h10M20 24h10M20 29h10" stroke="#fff" stroke-width="2"/></svg>
  <h3 class="abs">EASY CLAIMS PROCESS</h3>
  <p class="abs">Using CareVault Plus has never been easier. Just send us copies, scans or photos of your.</p>
  <span class="abs more">READ MORE</span>
</div>
<div class="abs card" style="left:517px">
  <svg class="abs icon" viewBox="0 0 50 50"><rect x="13" y="17" width="24" height="15" rx="2" transform="rotate(-20 25 25)" fill="none" stroke="#fff" stroke-width="2.2"/><text x="25" y="29" fill="#fff" font-size="11" font-weight="700" text-anchor="middle" font-family="Lato">$</text></svg>
  <h3 class="abs">ONE LOW MONTHLY FEE</h3>
  <p class="abs"><b style="color:#222">PLUS</b><br>Get a $5 bonus rebate each calendar quarter to use on home.</p>
  <span class="abs more">READ MORE</span>
</div>

<!-- welcome -->
<section class="abs welcome">
  <h2 class="abs">WELCOME TO <span>CAREVAULT PLUS</span></h2>
  <div class="abs video" role="img" aria-label="Video still: friends shopping together">
    <svg class="abs" style="left:78px;top:38px" width="34" height="34" viewBox="0 0 34 34"><circle cx="17" cy="17" r="15" fill="rgba(255,255,255,.3)" stroke="#fff" stroke-width="2"/><path d="M13 10l11 7-11 7z" fill="#fff"/></svg>
    <div class="abs video-bar">
      <svg width="186" height="13"><path d="M8 3l6 3.5-6 3.5z" fill="#ccc"/><rect x="24" y="6" width="56" height="2" fill="#666"/><rect x="118" y="3" width="60" height="7" rx="2" fill="#444"/><rect x="150" y="5" width="26" height="3" fill="#f0a020"/></svg>
    </div>
  </div>
  <p class="abs body">CareVault helps people cope with the complexities of modern life. We provide our customers with support and protection for what's really important to them, including their credit cards, personal information and identities. When these are lost, damaged or stolen we know that our customers need help to make things right. And that's precisely what we do.</p>
  <span class="abs read-more">READ MORE</span>
  <div class="abs pf">
    <div class="pf-head">PRODUCT FEATURES</div>
    <ul>
      <li>✔ Warranty Extension</li>
      <li>✔ Repair Bill Rebate</li>
      <li>✔ Product Return Guarantee</li>
      <li>✔ Price Protection</li>
      <li>✔ Restocking Fee Reimbursement</li>
    </ul>
  </div>
</section>

<!-- how it works -->
<div class="abs how-line"></div>
<div class="abs how-title">HOW IT WORKS</div>
<svg class="abs" style="left:0;top:820px" width="806" height="60"><path d="M222 30C260 10 310 12 345 30" stroke="#999" stroke-dasharray="5 3" fill="none"/><path d="M340 25l6 5-7 2" stroke="#999" fill="none"/><path d="M462 40C500 55 545 52 585 38" stroke="#999" stroke-dasharray="5 3" fill="none"/><path d="M578 34l7 4-6 5" stroke="#999" fill="none"/></svg>

<div class="abs step" style="left:112px"><svg width="98" height="98" viewBox="0 0 98 98"><rect x="28" y="40" width="44" height="33" rx="3" fill="#111"/><path d="M38 42v-8a12 12 0 0 1 24 0v8" stroke="#111" stroke-width="4" fill="none"/></svg></div>
<div class="abs step" style="left:352px"><svg width="98" height="98" viewBox="0 0 98 98"><rect x="32" y="24" width="34" height="46" fill="none" stroke="#111" stroke-width="4"/><text x="42" y="60" font-size="18" font-weight="700" fill="#111" font-family="Lato">$</text><path d="M52 42h9M52 50h9M52 58h9" stroke="#111" stroke-width="3"/></svg></div>
<div class="abs step" style="left:591px"><svg width="98" height="98" viewBox="0 0 98 98"><rect x="28" y="26" width="38" height="44" fill="none" stroke="#111" stroke-width="4"/><path d="M34 36h16M34 46h16M34 56h16" stroke="#111" stroke-width="3"/><rect x="54" y="33" width="6" height="6" fill="none" stroke="#111" stroke-width="2"/><rect x="54" y="43" width="6" height="6" fill="none" stroke="#111" stroke-width="2"/><rect x="54" y="53" width="6" height="6" fill="none" stroke="#111" stroke-width="2"/><path d="M70 32v40H34" stroke="#111" stroke-width="4" fill="none"/></svg></div>
<div class="abs step-label" style="left:84px">MAKE YOUR<br><span>PURCHASES</span></div>
<div class="abs step-label" style="left:324px">STORE YOUR<br><span>RECEIPTS</span></div>
<div class="abs step-label" style="left:564px">SUBMIT YOUR<br><span>CLAIMS</span></div>

<!-- footer -->
<footer class="abs footer"></footer>
<div class="abs fcol" style="left:96px;width:86px">
  <h4>QUICK LINKS</h4>
  <ul class="links"><li>Home</li><li>About Us</li><li>Product Features</li><li>How It Works</li><li>Privacy</li><li>Contact</li></ul>
</div>
<div class="abs fcol" style="left:214px;width:148px">
  <h4>CONTACT FORM</h4>
  <div class="field">👤 Name</div>
  <div class="field">✉ Email</div>
  <div class="field tall">✎ Address</div>
  <span class="subscribe">SUBSCRIBE</span>
</div>
<div class="abs fcol" style="left:395px;width:152px">
  <h4>LOCATION MAP</h4>
  <div class="map" style="margin-left:-3px" role="img" aria-label="Street map showing the office location"></div>
</div>
<div class="abs fcol" style="left:578px;width:133px">
  <h4>CONTACT INFO</h4>
  <div class="info">
    <div class="row"><svg width="11" height="13" viewBox="0 0 12 16"><path d="M6 0a6 6 0 0 0-6 6c0 4 6 10 6 10s6-6 6-10a6 6 0 0 0-6-6zm0 8.5A2.5 2.5 0 1 1 6 3.5a2.5 2.5 0 0 1 0 5z" fill="#eee"/></svg><span>CareVault Plus<br>ATTN: Member Services<br>P.O. Box 1200<br>Lakeview, MN 55000</span></div>
    <div class="row"><svg width="11" height="11" viewBox="0 0 24 24"><path fill="#eee" d="M6.6 10.8a15 15 0 0 0 6.6 6.6l2.2-2.2c.3-.3.7-.4 1-.2 1.1.4 2.3.6 3.6.6.6 0 1 .4 1 1V20c0 .6-.4 1-1 1A17 17 0 0 1 3 4c0-.6.4-1 1-1h3.5c.6 0 1 .4 1 1 0 1.3.2 2.5.6 3.6.1.3 0 .7-.2 1z"/></svg><span>(888) 555-0142</span></div>
    <div class="row"><svg width="11" height="9" viewBox="0 0 12 9"><rect width="12" height="9" fill="#eee"/><path d="M0 0l6 5 6-5" stroke="#3a3a3a" fill="none"/></svg><span>info@carevaultplus.example</span></div>
    <div class="row"><svg width="11" height="11" viewBox="0 0 12 12"><rect x="1" y="4" width="10" height="6" fill="#eee"/><rect x="3" y="1" width="6" height="3" fill="#eee"/></svg><span>0123 555 789</span></div>
  </div>
</div>
<div class="abs bottombar">
  <span class="abs copy">© 2014 CareVault Plus &nbsp;|&nbsp; All rights reserved</span>
  <span class="abs follow">Follow Us On :
    <svg width="46" height="10"><circle cx="5" cy="5" r="4" fill="#eee"/><circle cx="22" cy="5" r="4" fill="#eee"/><circle cx="39" cy="5" r="4" fill="#eee"/></svg>
  </span>
</div>

</body>
</html>
```